HARBORLINE MAILWORKS - DIRECT MAIL BUSINESS CARD

Harborline Mailworks, 418 E Birch Ave, NORMAN OK 73512 405-287-9046 email - dalew412@mailnest.example Owner Dale Wren Serving customers since 1989, Product - Direct mail marketing

Target Market(s)

Businesses,churches and non-profits

Industry/Entity Type

Marketing

Contact Information for Business Card

Dark blue UV coated card with white letters on front. Maybe add a sketch of a mail addressing machine. On the back either Dark blue or full color with the sketch of a postman throwing a letter towards a world globe, with the phrase reach your world. Or the postman throwing a letter towards a archery target with the phrase, reach your target market.

Font styles to use
Serif

Colors
0355a3

Requirements
Must have
• INFORMATION HARBORLINE MAILWORKS
• 418 E BIRCH AVE
• NORMAN OK 73512
• 405-287-9046
• dalew412@mailnest.example
• DALE WREN, OWNER
• DIRECT MAIL MARKETING
Nice to have
• SERVING CUSTOMERS SINCE 1989 SKETCH OF MAIL ADDRESSING EQUIPMENT, IN THE BACKGROUND, ON THE FRONT
• ON THE BACK, SKETCH OF POSTMAN THROWING LETTER TO THE WORLD
• GLOBE, WITH THE PHRASE, REACH YOUR WORLD, OR THE LETTER TO A TARGET, WITH PHRASE, REACH YOUR TARGET MARKET
Should not have
• PHOTOS OR FLOWERS

```html
<!DOCTYPE html>
<html lang="en">
<head>
<meta charset="utf-8">
<title>Harborline Mailworks – Business Card</title>
<link rel="stylesheet" href="https://fonts.googleapis.com/css2?family=Open+Sans:wght@400;600;700&display=swap">
<style>
  :root {
    --brand-blue: #0355a3;
    --band-dark: #2a2a2c;
    --card-paper: #ececea;
    --ink: #2f2f2f;
    --stage: #d9d9d9;
    --white: #ffffff;
  }
  * { box-sizing: border-box; margin: 0; padding: 0; }
  html, body {
    width: 1200px; height: 900px; overflow: hidden;
    background: var(--stage);
    font-family: "Open Sans", sans-serif;
    color: var(--ink);
  }
  .stage {
    width: 1200px; height: 900px;
    display: flex; flex-direction: column;
    align-items: center; justify-content: center; gap: 40px;
  }
  .card {
    position: relative;
    width: 700px; height: 400px;
    background: var(--card-paper);
    box-shadow: 0 8px 24px rgba(0,0,0,.25);
    overflow: hidden;
  }
  .card__band {
    position: absolute; left: 0; right: 0;
    background: var(--band-dark);
  }
  .card__band--top { top: 0; height: 22px; border-bottom: 5px solid var(--brand-blue); height: 27px; }
  .card__band--bottom { bottom: 0; height: 34px; border-top: 5px solid var(--brand-blue); }

  /* Back side */
  .card--back { display: flex; flex-direction: column; align-items: center; justify-content: center; }
  .target-art {
    width: 100px; height: 100px; border-radius: 50%;
    background: radial-gradient(circle, #f0a8a0 0%, #e8f1f4 45%, #5cc2c8 70%, #dfe6ea 100%);
    margin-bottom: 22px;
  }
  .tagline { font-size: 17px; font-weight: 400; letter-spacing: .3px; text-transform: uppercase; }

  /* Front side */
  .brand {
    position: absolute; left: 60px; top: 170px; width: 260px;
    display: flex; align-items: center; gap: 10px;
    font-size: 19px; font-weight: 400; color: var(--ink);
  }
  .brand__dot { width: 18px; height: 18px; border-radius: 50%; background: var(--brand-blue); flex: none; }

  .identity { position: absolute; left: 400px; top: 48px; right: 0; }
  .identity__name { font-size: 22px; font-weight: 700; letter-spacing: .2px; line-height: 1.15; }
  .identity__role { font-size: 17px; line-height: 1.25; text-transform: uppercase; }
  .identity__rule { margin-top: 6px; height: 2px; background: var(--brand-blue); margin-left: -6px; }

  .contacts { position: absolute; left: 400px; top: 158px; right: 10px; list-style: none; }
  .contact { display: flex; align-items: center; gap: 18px; margin-bottom: 18px; font-size: 16px; line-height: 1.2; }
  .contact__icon {
    width: 36px; height: 30px; border-radius: 6px;
    background: var(--brand-blue);
    display: flex; align-items: center; justify-content: center; flex: none;
  }
  .contact__icon svg { width: 18px; height: 18px; }
</style>
</head>
<body>
<main class="stage">

  <section class="card card--back" aria-label="Business card back">
    <div class="card__band card__band--top"></div>
    <div class="target-art" role="img" aria-label="Illustration of two customers inside a target with a magnifying glass"></div>
    <p class="tagline">Reach your target market</p>
    <div class="card__band card__band--bottom"></div>
  </section>

  <section class="card card--front" aria-label="Business card front">
    <div class="card__band card__band--top"></div>

    <div class="brand">
      <span class="brand__dot"></span>
      <span class="brand__name">Harborline Mailworks</span>
    </div>

    <div class="identity">
      <h1 class="identity__name">DALE WREN</h1>
      <p class="identity__role">Owner</p>
      <p class="identity__role">Direct Mail Marketing</p>
      <div class="identity__rule"></div>
    </div>

    <ul class="contacts">
      <li class="contact">
        <span class="contact__icon">
          <svg viewBox="0 0 24 24" fill="var(--white)"><path d="M6.6 10.8a15.1 15.1 0 0 0 6.6 6.6l2.2-2.2c.3-.3.7-.4 1-.2 1.1.4 2.3.6 3.6.6.6 0 1 .4 1 1V20c0 .6-.4 1-1 1C10.6 21 3 13.4 3 4c0-.6.4-1 1-1h3.5c.6 0 1 .4 1 1 0 1.3.2 2.5.6 3.6.1.3 0 .7-.2 1z"/></svg>
        </span>
        <span>405-287-9046</span>
      </li>
      <li class="contact">
        <span class="contact__icon">
          <svg viewBox="0 0 24 24" fill="none" stroke="var(--white)" stroke-width="1.8"><circle cx="12" cy="12" r="9"/><ellipse cx="12" cy="12" rx="4" ry="9"/><path d="M3 12h18M5 7h14M5 17h14"/></svg>
        </span>
        <span>dalew412@mailnest.example<br>www.harborlinemail.example</span>
      </li>
      <li class="contact">
        <span class="contact__icon">
          <svg viewBox="0 0 24 24" fill="var(--white)"><path d="M12 2a7 7 0 0 0-7 7c0 5 7 13 7 13s7-8 7-13a7 7 0 0 0-7-7zm0 9.5A2.5 2.5 0 1 1 12 6.5a2.5 2.5 0 0 1 0 5z"/></svg>
        </span>
        <span>Harborline Mailworks,418 E BIRCH AVE<br>NORMAN OK 73512</span>
      </li>
    </ul>

    <div class="card__band card__band--bottom"></div>
  </section>

</main>
</body>
</html>
```